Ironvale Holdings Business card

We need a an amazing matte black and gold card! W are a finance investing company so we want something that's eye catching and sleek. We want it to be attractive and sleek and represent money. Heck with would like the letters and lgo to be printed as 24k gold one day. We have the logo added so please use the color scheme with the logo and have that beautifully placed on one side.

Target Market(s)

Investors of all ages

Industry/Entity Type

Financial

Contact Information for Business Card

Black and matte with gold lettering follow logo colrs please.

Font styles to use
Other font styles liked:
• you decide

Colors

Designer to choose colors to be used in the design.

Requirements
Must have
• Matte Black and Gold, logo on one side. job title and name , website, phone number and email address on the other side
Nice to have
• Matte black and crisp finish to attract investors
Should not have
• playful, very professional!

```html
<!DOCTYPE html>
<html lang="en">
<head>
<meta charset="utf-8">
<title>Ironvale Holdings Business Card</title>
<link rel="stylesheet" href="https://fonts.googleapis.com/css2?family=Lato:wght@400;700;900&display=swap">
<style>
  :root {
    --backdrop: #2b2b2d;
    --card: #0a0b0d;
    --gold: #c09a2c;
    --gold-light: #d8b446;
    --white: #f2f2f2;
  }
  * { margin: 0; padding: 0; box-sizing: border-box; }
  html, body {
    width: 1200px; height: 1133px; overflow: hidden;
    background: var(--backdrop);
    font-family: "Lato", Arial, sans-serif;
  }
  .canvas { position: relative; width: 1200px; height: 1133px; }
  .card {
    position: absolute;
    width: 820px; height: 470px;
    background: var(--card);
    box-shadow: 0 18px 40px rgba(0,0,0,0.55);
  }
  .card-front { left: 90px; top: 70px; }
  .card-back { left: 290px; top: 600px; }

  .name-accent {
    position: absolute; left: 30px; top: 98px;
    width: 14px; height: 72px; background: var(--gold);
  }
  .holder-name {
    position: absolute; left: 70px; top: 92px;
    font-weight: 900; font-size: 36px; letter-spacing: 0.5px;
    color: var(--gold-light); text-transform: uppercase;
  }
  .holder-title {
    position: absolute; left: 72px; top: 136px;
    font-size: 22px; color: var(--white);
  }
  .address {
    position: absolute; left: 100px; top: 250px;
    font-size: 21px; line-height: 28px; color: var(--white);
  }
  .contact-list {
    position: absolute; left: 100px; top: 330px;
    list-style: none;
  }
  .contact-list li {
    display: flex; align-items: center; gap: 14px;
    height: 32px; font-size: 21px; color: var(--white);
  }
  .contact-list svg { width: 20px; height: 20px; flex: none; }

  .brand {
    position: absolute;
    font-weight: 700; color: var(--gold);
    text-transform: uppercase; text-align: center; line-height: 1.1;
  }
  .card-front .brand { right: 70px; top: 110px; font-size: 40px; letter-spacing: 3px; }
  .card-back .brand { left: 0; right: 0; top: 170px; font-size: 58px; letter-spacing: 5px; }
</style>
</head>
<body>
<div class="canvas">
  <section class="card card-front">
    <div class="name-accent"></div>
    <h1 class="holder-name">Daniel Reyes</h1>
    <p class="holder-title">Director</p>
    <p class="address">Address first line 1234<br>4567second line</p>
    <ul class="contact-list">
      <li>
        <svg viewBox="0 0 24 24" aria-hidden="true"><path fill="var(--gold)" d="M6.6 10.8a15.1 15.1 0 0 0 6.6 6.6l2.2-2.2c.3-.3.7-.4 1-.2 1.1.4 2.3.6 3.6.6.6 0 1 .4 1 1V20c0 .6-.4 1-1 1A17 17 0 0 1 3 4c0-.6.4-1 1-1h3.5c.6 0 1 .4 1 1 0 1.3.2 2.5.6 3.6.1.3 0 .7-.2 1z"/></svg>
        +1 555 014 2290
      </li>
      <li>
        <svg viewBox="0 0 24 24" aria-hidden="true"><rect x="2" y="5" width="20" height="14" fill="var(--gold)"/><path d="M2 5l10 8 10-8" fill="none" stroke="var(--card)" stroke-width="1.6"/></svg>
        contact@ironvaleholdings.com
      </li>
      <li>
        <svg viewBox="0 0 24 24" aria-hidden="true"><g fill="none" stroke="var(--gold)" stroke-width="1.8"><circle cx="12" cy="12" r="9.5"/><ellipse cx="12" cy="12" rx="4.5" ry="9.5"/><path d="M2.5 12h19M4 7h16M4 17h16"/></g></svg>
        www.ironvaleholdings.com
      </li>
    </ul>
    <div class="brand">Ironvale<br>Holdings</div>
  </section>

  <section class="card card-back">
    <div class="brand">Ironvale<br>Holdings</div>
  </section>
</div>
</body>
</html>
```